Post it Note design

POST-IT NOTE DESIGN (CONTENT)
Size recommended: 4x6 for handwriting space.
Header (Bold):
Lighting Issue Detected on Your Property
Sub-header:
During our routine night inspection, we noted the following item(s):
Checkbox List:
⬜ Building Lights Out
⬜ Pole Lights Out
⬜ Sign Not Illuminated
⬜ Other ________________________
Action Line:
We can provide a quote or dispatch service right away.
Area for notes
Contact Block (Bold & Centered):
Brovane Fixture Inc.
Service@BrovaneFixture.com
www.BrovaneFixture.com
877-514-0862
Industry/Entity Type
Electrical lighting
Colors
Designer to choose colors to be used in the design.
Look and feel
Each slider illustrates characteristics of the customer's brand and the style your logo design should communicate.

```html
<!DOCTYPE html>
<html lang="en">
<head>
<meta charset="utf-8">
<title>Lighting Issue Detected – Brovane Fixture Inc.</title>
<link rel="stylesheet" href="https://fonts.googleapis.com/css2?family=Montserrat:ital,wght@0,500;0,700;1,700&family=Lato:wght@400;700&display=swap">
<style>
  :root {
    --page-bg: #f2f2f2;
    --card-bg: #ffffff;
    --brand-red: #c8102e;
    --alert-red: #e8202a;
    --navy: #2a3341;
    --footer-dark: #232833;
    --band-blue: #2e3a8c;
    --field-bg: #f1f1f3;
    --notes-bg: #f7f7fa;
    --notes-border: #d3d3dc;
    --ink: #2b2b33;
    --dots: #8a8fa0;
    --white: #ffffff;
  }
  * { box-sizing: border-box; margin: 0; padding: 0; }
  html, body {
    width: 1200px; height: 1137px; overflow: hidden;
    background: var(--page-bg);
    font-family: "Lato", Arial, sans-serif;
    color: var(--ink);
  }
  .note {
    position: absolute; left: 266px; top: 84px;
    width: 658px; height: 986px;
    background: var(--card-bg);
    box-shadow: 0 1px 4px rgba(0,0,0,.15);
    overflow: hidden;
  }
  .note-header {
    position: absolute; left: 0; top: 0; width: 100%; height: 191px;
    background: var(--brand-red);
  }
  .brand-box {
    position: absolute; left: 23px; top: 34px; width: 228px; height: 125px;
    background: #eeeeee;
    display: flex; align-items: center; justify-content: center;
  }
  .brand-name {
    font-family: "Montserrat", Arial, sans-serif; font-weight: 700;
    color: var(--brand-red); font-size: 25px; line-height: 1.15; text-align: center;
  }
  .headline {
    position: absolute; left: 250px; top: 0; width: 380px; height: 191px;
    font-family: "Montserrat", Arial, sans-serif; color: var(--white); text-align: center;
    font-weight: 700;
  }
  .headline span { position: absolute; display: block; }
  .headline-top {
    left: 0; top: 28px; width: 100%;
    font-size: 40px; line-height: 44px; letter-spacing: .5px;
  }
  .headline-badge {
    left: 28px; top: 80px; width: 339px; height: 43px;
    background: var(--navy); font-size: 38px; line-height: 44px; letter-spacing: 1px;
  }
  .headline-sub {
    left: 0; top: 126px; width: 100%;
    font-weight: 500; font-size: 36px; line-height: 40px;
  }

  .field {
    position: absolute; top: 219px; height: 41px;
    background: var(--field-bg); border: 2px solid var(--navy);
    font-size: 21px; line-height: 37px; padding-left: 36px; color: var(--ink);
  }
  .field-date { left: 34px; width: 290px; }
  .field-time { left: 334px; width: 289px; padding-left: 30px; }

  .intro {
    position: absolute; left: 33px; top: 282px; width: 610px;
    font-size: 23px; line-height: 27px;
  }
  .checklist { position: absolute; left: 35px; top: 356px; width: 590px; list-style: none; }
  .checklist li {
    display: flex; align-items: center; height: 46px;
    font-size: 27px; font-weight: 700; color: var(--ink);
  }
  .checkbox {
    width: 27px; height: 27px; border: 2.5px solid var(--navy); border-radius: 4px;
    margin-right: 17px; flex: none;
  }
  .fill-line {
    flex: 1; border-bottom: 2px dotted var(--dots); height: 18px;
    margin-left: 8px; margin-right: 24px;
  }

  .notes {
    position: absolute; left: 37px; top: 553px; width: 590px; height: 147px;
    background: var(--notes-bg); border: 1px solid var(--notes-border);
    display: grid; grid-template-columns: 1fr 1fr; grid-auto-rows: 39px;
    column-gap: 7px; align-content: start;
    padding: 0 26px 0 26px;
  }
  .notes span { border-bottom: 2px dotted var(--dots); }

  .action-band {
    position: absolute; left: 36px; top: 713px; width: 588px; height: 46px;
    background: var(--band-blue); color: var(--white);
    font-size: 20px; line-height: 46px; text-align: center;
  }
  .action-band strong { font-weight: 700; font-size: 21px; }

  .call-today {
    position: absolute; left: 30px; top: 808px;
    font-family: "Montserrat", Arial, sans-serif; font-style: italic; font-weight: 700;
    font-size: 28px; line-height: 34px; color: var(--brand-red);
  }
  .contact-bar {
    position: absolute; left: 0; top: 849px; width: 100%; height: 137px;
    background: var(--footer-dark);
  }
  .phone {
    position: absolute; left: 18px; top: 22px; display: flex; align-items: center;
    font-family: "Montserrat", Arial, sans-serif; font-weight: 700; font-size: 36px; color: var(--alert-red);
  }
  .phone svg { width: 33px; height: 33px; margin-right: 12px; }
  .contact-lines {
    position: absolute; left: 17px; top: 72px; color: var(--white);
    font-size: 19px; line-height: 25px;
  }
  .service-photo {
    position: absolute; left: 356px; top: 778px; width: 302px; height: 208px;
    background: linear-gradient(165deg, rgba(220,224,230,.85) 0%, rgba(140,146,156,.6) 40%, rgba(50,56,68,.85) 100%);
    border-radius: 70px 0 0 0;
  }
</style>
</head>
<body>
  <main class="note">
    <header class="note-header">
      <div class="brand-box"><span class="brand-name">Brovane<br>Fixture Inc.</span></div>
      <h1 class="headline">
        <span class="headline-top">LIGHTING ISSUE</span>
        <span class="headline-badge">DETECTED</span>
        <span class="headline-sub">on Your Property</span>
      </h1>
    </header>

    <div class="field field-date">DATE:</div>
    <div class="field field-time">TIME:</div>

    <p class="intro">During our routine night inspection, we noted the following item(s):</p>

    <ul class="checklist">
      <li><span class="checkbox"></span>Building Lights Out</li>
      <li><span class="checkbox"></span>Pole Lights Out</li>
      <li><span class="checkbox"></span>Sign Not Illuminated</li>
      <li><span class="checkbox"></span>Other:<span class="fill-line"></span></li>
    </ul>

    <div class="notes" aria-label="Notes area">
      <span></span><span></span><span></span><span></span><span></span><span></span>
    </div>

    <p class="action-band">We can provide a <strong>quote or dispatch service</strong> right away.</p>

    <p class="call-today">Call Us Today</p>

    <footer class="contact-bar">
      <div class="phone">
        <svg viewBox="0 0 34 34" aria-hidden="true">
          <circle cx="17" cy="17" r="15.5" fill="none" stroke="#ffffff" stroke-width="2"/>
          <path d="M11.5 9.5c.8-.8 1.8-.6 2.3.2l1.6 2.6c.4.7.2 1.5-.4 2l-1 .8c.9 2 2.5 3.7 4.5 4.6l.8-1c.5-.6 1.3-.8 2-.4l2.6 1.6c.8.5 1 1.5.2 2.3l-1.2 1.2c-1 1-2.6 1.2-4 .5-3.7-1.8-6.7-4.8-8.5-8.5-.7-1.4-.5-3 .5-4z" fill="#ffffff"/>
          <path d="M20 9.5a5 5 0 0 1 4.5 4.5M20 6.5a8 8 0 0 1 7.5 7.5" fill="none" stroke="#ffffff" stroke-width="1.6" stroke-linecap="round"/>
        </svg>
        877-514-0862
      </div>
      <div class="contact-lines">
        <p>Service@BrovaneFixture.com</p>
        <p>www.BrovaneFixture.com</p>
      </div>
    </footer>

    <div class="service-photo" role="img" aria-label="Photo of a bucket truck and parking lot pole light fixtures"></div>
  </main>
</body>
</html>
```